Brightoak Business Card

Professional Business Card Design required using the attached contact information.

Contact information can be rearranged as required.

The company is a new start up venture developing solar systems, the branding should be in keeping with that of one of the investors whose website is as follows https://www.corvellan.com/

```html
<!DOCTYPE html>
<html lang="en">
<head>
<meta charset="utf-8">
<title>Brightoak Renewables – Business Card</title>
<link href="https://fonts.googleapis.com/css2?family=Montserrat:wght@400;500;600&display=swap" rel="stylesheet">
<style>
  :root {
    --backdrop: #e4e4e4;
    --forest: #1c5646;
    --paper: #ffffff;
    --ink: #141414;
    --card-shadow: 0 6px 14px rgba(0,0,0,0.28);
  }
  * { margin: 0; padding: 0; box-sizing: border-box; }
  html, body {
    width: 1125px;
    height: 1200px;
    overflow: hidden;
    background: var(--backdrop);
    font-family: "Montserrat", Arial, sans-serif;
  }
  .card {
    position: absolute;
    left: 150px;
    width: 826px;
    height: 471px;
    box-shadow: var(--card-shadow);
  }
  .card--front {
    top: 103px;
    background: var(--forest);
    color: var(--paper);
  }
  .card--back {
    top: 625px;
    background: var(--paper);
    display: flex;
    align-items: center;
    justify-content: center;
  }
  .holder-name {
    position: absolute;
    left: 44px;
    top: 230px;
    font-size: 23px;
    font-weight: 500;
    letter-spacing: 0.3px;
  }
  .address {
    position: absolute;
    left: 44px;
    top: 293px;
    font-size: 17px;
    line-height: 22.5px;
    font-style: normal;
    font-weight: 400;
  }
  .contact-list {
    position: absolute;
    left: 44px;
    top: 371px;
    list-style: none;
    font-size: 17px;
    line-height: 23px;
  }
  .contact-list li {
    display: flex;
    align-items: center;
    gap: 9px;
  }
  .contact-icon {
    width: 14px;
    height: 14px;
    fill: var(--paper);
    flex: none;
  }
  .wordmark {
    font-size: 29px;
    font-weight: 500;
    letter-spacing: 2.2px;
    color: var(--ink);
  }
</style>
</head>
<body>
  <section class="card card--front">
    <h1 class="holder-name">DANIEL CORWIN</h1>
    <address class="address">
      Brightoak Renewables LLC<br>
      318 Harbor Street,<br>
      Salem, MA 01970
    </address>
    <ul class="contact-list">
      <li>
        <svg class="contact-icon" viewBox="0 0 24 24" aria-hidden="true"><path d="M6.6 10.8c1.4 2.8 3.8 5.1 6.6 6.6l2.2-2.2c.3-.3.7-.4 1-.2 1.1.4 2.3.6 3.6.6.6 0 1 .4 1 1V20c0 .6-.4 1-1 1C10.6 21 3 13.4 3 4c0-.6.4-1 1-1h3.5c.6 0 1 .4 1 1 0 1.3.2 2.5.6 3.6.1.3 0 .7-.2 1z"/></svg>
        +1 (555) 014-2276
      </li>
      <li>
        <svg class="contact-icon" viewBox="0 0 24 24" aria-hidden="true"><path d="M3 6h18v12H3z M3 6l9 7 9-7" /><path d="M3 6l9 7 9-7v1.5l-9 7-9-7z" fill="#1c5646"/></svg>
        daniel.corwin@brightoak-renewables.com
      </li>
      <li>
        <svg class="contact-icon" viewBox="0 0 24 24" aria-hidden="true"><circle cx="12" cy="12" r="10"/><path d="M7 8c2 0 3 1 3 3s-2 2-2 4M14 5c0 2 2 2 3 3s0 3 2 4" stroke="#1c5646" stroke-width="1.6" fill="none"/></svg>
        www.brightoak-renewables.com
      </li>
    </ul>
  </section>

  <section class="card card--back">
    <p class="wordmark">BRIGHTOAK RENEWABLES</p>
  </section>
</body>
</html>
```